Tello Haulage Junk Removal Postcard

I am looking to have a postcard made for my junk removal company. Details:
size: 6"x9"
I would like to keep it clean and simple. Our company colors are pink, blue and white. You can find the colors and info on the company and what we do on our website which is www.tellohaulage.example .
I've attached a sample of a postcard that was made on ArtHive for another junk removal company. I like the way the attached one looks.

```html
<!DOCTYPE html>
<html lang="en">
<head>
<meta charset="utf-8">
<title>Junk Removal Services Postcard</title>
<link rel="stylesheet" href="https://fonts.googleapis.com/css2?family=Arimo:wght@400;700&display=swap">
<style>
  :root {
    --navy: #063f83;
    --navy-deep: #053a78;
    --pink: #f07ad8;
    --pink-band: #c471c4;
    --orchid: #c36fc6;
    --white: #ffffff;
    --photo-dark: #2a2a2c;
    --photo-mid: #3b3c3f;
  }
  html, body {
    margin: 0;
    padding: 0;
    width: 1200px;
    height: 800px;
    overflow: hidden;
    background: var(--white);
  }
  .postcard {
    display: block;
    width: 1200px;
    height: 800px;
    font-family: "Arimo", Arial, sans-serif;
  }
  .headline { font-weight: 700; fill: var(--white); }
  .tagline { font-size: 16px; fill: var(--navy); letter-spacing: 0.3px; }
  .offer { font-weight: 700; fill: var(--pink); font-size: 62px; }
  .title-main { font-size: 112px; letter-spacing: 2px; }
  .title-sub { font-size: 37px; fill: var(--white); letter-spacing: 0.5px; }
  .section-title { font-size: 33px; }
  .section-title--small { font-size: 28px; }
  .body-copy { font-size: 15px; fill: var(--white); }
  .service-list { font-size: 16px; fill: var(--white); }
  .bullet { fill: var(--orchid); }
  .badge-ring { fill: none; stroke: var(--pink); stroke-width: 3; }
  .badge-text { font-size: 15px; fill: var(--white); }
  .badge-text--small { font-size: 12px; }
  .call-label { font-size: 22px; fill: var(--white); }
  .call-number { font-size: 28px; font-weight: 700; fill: var(--white); letter-spacing: 1px; }
  .web-address { font-size: 17px; fill: var(--navy); letter-spacing: 0.3px; }
  .outline-pink { fill: none; stroke: var(--pink); stroke-width: 3; }
</style>
</head>
<body>
<svg class="postcard" viewBox="0 0 1000 667" xmlns="http://www.w3.org/2000/svg">
  <defs>
    <linearGradient id="photoTone" x1="0" y1="0" x2="1" y2="1">
      <stop offset="0" stop-color="var(--photo-mid)"/>
      <stop offset="1" stop-color="var(--photo-dark)"/>
    </linearGradient>
  </defs>

  <!-- hero photo area -->
  <rect class="hero-photo" x="0" y="0" width="1000" height="667" fill="url(#photoTone)" role="img" aria-label="Photo of a junk removal truck loaded with old furniture and appliances"/>

  <!-- blue panels -->
  <polygon class="panel" fill="var(--navy)" points="0,310 355,310 380,330 545,135 1000,135 1000,667 0,667"/>

  <!-- decorative stripes -->
  <polygon class="stripe-band" fill="var(--pink-band)" opacity="0.75" points="120,296 360,296 610,598 548,598 335,320 120,320"/>
  <polygon class="stripe-band" fill="var(--pink-band)" opacity="0.7" points="560,0 622,0 688,82 640,112"/>
  <polygon class="outline-pink" points="515,0 548,0 668,186 628,214"/>
  <polygon class="outline-pink" points="383,522 420,500 543,667 494,667"/>

  <!-- tagline banner -->
  <polygon fill="var(--white)" points="0,0 460,0 485,50 0,50"/>
  <text class="tagline" x="35" y="35">THE WORLD’S LARGEST JUNK REMOVAL SERVICE</text>

  <!-- offer box -->
  <rect x="710" y="-3" width="230" height="198" fill="var(--navy)" class="outline-pink"/>
  <rect x="710" y="-3" width="230" height="198" fill="var(--navy)"/>
  <rect x="710" y="-3" width="230" height="198" class="outline-pink"/>
  <text class="offer" x="825" y="84" text-anchor="middle">50%</text>
  <text class="offer" x="821" y="156" text-anchor="middle">OFF</text>

  <!-- title -->
  <text class="headline title-main" x="33" y="170">JUNK</text>
  <text class="title-sub" x="36" y="242">REMOVAL SERVICES</text>

  <!-- why choose us -->
  <text class="headline section-title" x="598" y="280">WHY CHOOSE US?</text>
  <text class="body-copy" text-anchor="end">
    <tspan x="948" y="313">Lorem ipsum dolor sit amet, consectetur adipisc-</tspan>
    <tspan x="948" y="334">ing elit. Vitae amet sed pretium interdum facilisis</tspan>
    <tspan x="948" y="355">nisl turpis. Id viverra faucibus justo, nulla orci</tspan>
    <tspan x="948" y="376">non, enim parturient sapien.</tspan>
  </text>

  <!-- what we do -->
  <text class="headline section-title--small" x="35" y="394">WHAT WE DO?</text>
  <g class="service-list">
    <rect class="bullet" x="35" y="419" width="18" height="18"/>
    <text x="63" y="432">Lorem ipsum dolor sit amet, con</text>
    <rect class="bullet" x="35" y="443" width="18" height="18"/>
    <text x="63" y="456">Lorem ipsum dolor sit amet, con</text>
    <rect class="bullet" x="35" y="469" width="18" height="18"/>
    <text x="63" y="481">Lorem ipsum dolor sit amet, con</text>
    <rect class="bullet" x="35" y="494" width="18" height="18"/>
    <text x="63" y="507">Lorem ipsum dolor sit amet, con</text>
  </g>

  <!-- feature badges -->
  <circle class="badge-ring" cx="633" cy="505" r="50"/>
  <text class="badge-text" text-anchor="middle"><tspan x="633" y="501">Same Day</tspan><tspan x="633" y="520">Service</tspan></text>
  <circle class="badge-ring" cx="775" cy="505" r="50"/>
  <text class="badge-text badge-text--small" text-anchor="middle"><tspan x="775" y="494">Professional</tspan><tspan x="775" y="509">Experienced and</tspan><tspan x="775" y="524">Reliable</tspan></text>
  <circle class="badge-ring" cx="909" cy="505" r="50"/>
  <text class="badge-text" text-anchor="middle"><tspan x="909" y="500">Best Price</tspan><tspan x="909" y="519">Guaranteed</tspan></text>

  <!-- call box -->
  <rect class="outline-pink" x="-3" y="563" width="336" height="94"/>
  <text class="call-label" x="160" y="596" text-anchor="middle">CALL US NOW</text>
  <text class="call-number" x="160" y="634" text-anchor="middle">000000000</text>

  <!-- web address band -->
  <polygon fill="var(--white)" points="558,605 1000,605 1000,667 600,667"/>
  <text class="web-address" x="787" y="639" text-anchor="middle">WWW.HAULAWAYJUNK.EXAMPLE</text>
</svg>
</body>
</html>
```